Label Design for a sexy ladies 5 pocket skinny

We need modern packaging design for women's skinny 5 pocket pants for a brand name Tarnel. All kinds of packaging designs are welcome.
The pant is folded and packaged in a poly bag. We require a label design for the brand name Tarnel. The main label will be attached by a string on the belt loop. the size of that label will 25cm in length and 10cm wide. This is the first label the customer see's when she picks up the garment. Therefore, we require an eye catching design for that. If required it could have certain information about the pant on the main label such as Comfort fit, Wrinkle-resistant, machine washable, luxury fabric. But, if you feel that adding the above information spoils the design of the label then it is not a must to include the above information. On the back of the label we like to include the information that this pant was manufactured in an Oskel Platinum certified green plant and hence the damage to the environment because of the plant is nill.
The second label is attached on to the waist band and the purpose of that label is to include the size of the pant such 32x32. The size of that label is 8cm in length and 4cm in width. There is no design on the back on this label it has to be blank.
Sample is given for what we currently use for our mens chino pant. we are looking for something very different.
Reason: because there was a delay in the project being approved by pixel harbor.
Environment

```html
<!DOCTYPE html>
<html lang="en">
<head>
<meta charset="utf-8">
<title>Tarnel – Ladies Skinny Label Set</title>
<link rel="stylesheet" href="https://fonts.googleapis.com/css2?family=Oswald:wght@500;700&family=Josefin+Sans:wght@400;600;700&family=Questrial&display=swap">
<style>
  :root {
    --board-light: #ffffff;
    --board-dark: #d6d6d6;
    --navy: #141a4c;
    --navy-deep: #0e1236;
    --white: #ffffff;
    --caption: #1a1a1a;
    --forest: #2f5a22;
    --meadow: #8fbf3a;
    --sky: #7fc7e0;
    --shadow: rgba(0,0,0,0.45);
  }
  html, body {
    margin: 0;
    padding: 0;
    width: 1200px;
    height: 1000px;
    overflow: hidden;
  }
  body {
    position: relative;
    background: radial-gradient(ellipse at 50% 40%, var(--board-light) 0%, #f1f1f1 45%, var(--board-dark) 100%);
    font-family: "Josefin Sans", sans-serif;
  }

  .label {
    position: absolute;
    box-shadow: 4px 5px 8px var(--shadow);
    overflow: hidden;
  }
  .caption {
    position: absolute;
    font-family: "Questrial", sans-serif;
    font-size: 19px;
    color: var(--caption);
    letter-spacing: 0.5px;
    text-align: center;
    white-space: nowrap;
    transform: translateX(-50%);
  }

  /* ---------- Hang tag, front ---------- */
  .tag-front {
    left: 126px; top: 90px; width: 310px; height: 775px;
  }
  .tag-front .scenery {
    position: absolute; inset: 0;
    background:
      linear-gradient(180deg, rgba(20,40,70,0.55) 0%, rgba(0,0,0,0) 18%),
      linear-gradient(90deg, var(--forest) 0%, #4f8a2b 40%, var(--meadow) 62%, var(--sky) 80%, #cfe8ef 100%);
  }
  .brand-name {
    position: absolute;
    left: 215px; top: 290px;
    transform: translate(-50%, -50%) rotate(90deg);
    font-family: "Oswald", sans-serif;
    font-weight: 700;
    font-size: 96px;
    line-height: 1;
    letter-spacing: 4px;
    color: var(--white);
    white-space: nowrap;
  }
  .product-line {
    position: absolute;
    font-family: "Oswald", sans-serif;
    font-weight: 500;
    color: var(--white);
    line-height: 1.0;
    letter-spacing: 2px;
    text-align: left;
    white-space: nowrap;
  }
  .tag-front .product-line {
    left: 70px; top: 508px;
    font-size: 25px;
    transform: rotate(-11deg);
  }
  .chevrons { position: absolute; }

  /* ---------- Hang tag, back ---------- */
  .tag-back {
    left: 452px; top: 90px; width: 311px; height: 775px;
    background: linear-gradient(180deg, var(--navy) 0%, var(--navy) 55%, #1d2a3c 78%, var(--navy-deep) 100%);
    color: var(--white);
  }
  .tag-back .product-line {
    left: 78px; top: 32px;
    font-size: 22px;
    transform: rotate(-8deg);
  }
  .garment-sketch {
    position: absolute;
    left: 14px; top: 115px; width: 283px; height: 365px;
    background: linear-gradient(180deg, rgba(255,255,255,0.06), rgba(255,255,255,0.02));
  }
  .features {
    position: absolute;
    left: 0; right: 0; top: 497px;
    text-align: center;
  }
  .feature {
    font-weight: 600;
    text-transform: uppercase;
    letter-spacing: 1.2px;
    line-height: 1;
    margin: 0 auto;
  }
  .feature--comfort {
    display: inline-block;
    font-size: 17px;
    padding: 4px 2px 3px;
    border-top: 1.5px solid var(--white);
    border-bottom: 1.5px solid var(--white);
  }
  .feature--wrinkle { font-size: 15px; margin-top: 10px; }
  .feature--wash { font-size: 15px; margin-top: 8px; }
  .feature--fabric {
    display: inline-block;
    font-size: 13px;
    letter-spacing: 2px;
    padding: 4px 8px 2px;
    margin-top: 10px;
    border-top: 1.5px solid var(--white);
    border-bottom: 1.5px solid var(--white);
  }
  .dot-row {
    position: absolute; left: 0; right: 0;
    text-align: center;
    font-size: 14px;
    letter-spacing: 5px;
    line-height: 1;
  }
  .eco-statement {
    position: absolute;
    left: 40px; right: 40px; top: 662px;
    margin: 0;
    font-family: "Josefin Sans", sans-serif;
    font-size: 13px;
    font-variant: small-caps;
    text-transform: none;
    letter-spacing: 1.2px;
    line-height: 15px;
    text-align: justify;
    text-align-last: center;
  }

  /* ---------- Waist band labels ---------- */
  .size-label {
    background: linear-gradient(135deg, var(--navy) 0%, #1b2350 60%, #232a3a 100%);
    color: var(--white);
    font-family: "Oswald", sans-serif;
  }
  .size-label .stitch {
    position: absolute; inset: 6px;
    border: 1px dashed rgba(255,255,255,0.75);
    border-radius: 3px;
  }
  .size-wide {
    left: 820px; top: 90px; width: 247px; height: 122px;
  }
  .size-wide .size-row {
    position: absolute; left: 20px; top: 14px;
    display: flex; align-items: center;
    height: 94px;
  }
  .size-wide .num { font-size: 78px; font-weight: 700; line-height: 1; }
  .size-wide .num--small { font-size: 56px; }
  .size-wide .dim {
    writing-mode: vertical-rl;
    transform: rotate(180deg);
    font-size: 9px; font-weight: 500; letter-spacing: 1px;
    margin: 0 2px;
    align-self: flex-end;
    margin-bottom: 12px;
  }
  .size-wide .times { font-size: 34px; font-weight: 500; margin: 6px 6px 0; }

  .size-tall {
    left: 885px; top: 278px; width: 125px; height: 249px;
    text-align: center;
  }
  .size-tall .num { display: block; font-weight: 700; line-height: 1; }
  .size-tall .num--waist { font-size: 78px; margin-top: 16px; }
  .size-tall .num--length { font-size: 56px; margin-top: 10px; }
  .size-tall .dim { display: block; font-size: 11px; font-weight: 500; letter-spacing: 1px; line-height: 1; }
  .size-tall .dim--waist { text-align: left; padding-left: 22px; margin-top: 0; }
  .size-tall .times { display: block; font-size: 30px; font-weight: 500; line-height: 1; margin-top: 10px; }
</style>
</head>
<body>

  <!-- Hang tag front -->
  <section class="label tag-front">
    <div class="scenery" role="img" aria-label="Photograph of a pine forest by a lake under a bright cloudy sky, with a moose grazing in the foreground"></div>
    <div class="brand-name">TARNEL</div>
    <svg class="chevrons" style="left:372px; top:500px;" width="36" height="26" viewBox="0 0 36 26" aria-hidden="true">
      <polyline points="2,4 16,10 4,20" fill="none" stroke="#ffffff" stroke-width="3"/>
      <polyline points="16,2 32,9 18,20" fill="none" stroke="#ffffff" stroke-width="3"/>
    </svg>
    <div class="product-line">LADIES SKINNY<br>5 POCKET PANTS</div>
    <svg class="chevrons" style="left:12px; top:552px;" width="40" height="28" viewBox="0 0 40 28" aria-hidden="true">
      <polyline points="36,4 20,14 34,24" fill="none" stroke="#ffffff" stroke-width="3"/>
      <polyline points="22,2 4,14 20,26" fill="none" stroke="#ffffff" stroke-width="3"/>
    </svg>
  </section>
  <div class="caption" style="left:288px; top:878px;">FRONT LABEL</div>

  <!-- Hang tag back -->
  <section class="label tag-back">
    <svg class="chevrons" style="left:26px; top:62px;" width="46" height="26" viewBox="0 0 46 26" aria-hidden="true">
      <polyline points="42,6 24,14 40,22" fill="none" stroke="#c9cbe0" stroke-width="2.5"/>
      <polyline points="26,4 6,14 24,24" fill="none" stroke="#c9cbe0" stroke-width="2.5"/>
    </svg>
    <div class="product-line">LADIES SKINNY<br>5 POCKET PANTS</div>
    <svg class="chevrons" style="left:246px; top:30px;" width="46" height="26" viewBox="0 0 46 26" aria-hidden="true">
      <polyline points="4,4 22,12 6,22" fill="none" stroke="#c9cbe0" stroke-width="2.5"/>
      <polyline points="20,2 40,11 22,22" fill="none" stroke="#c9cbe0" stroke-width="2.5"/>
    </svg>

    <div class="garment-sketch" role="img" aria-label="Line drawing of skinny five pocket jeans, front and back views"></div>

    <div class="features">
      <div class="feature feature--comfort">Comfort Fit</div>
      <div class="feature feature--wrinkle">—Wrinkle-Resistant—</div>
      <div class="feature feature--wash">~ Machine Washable ~</div>
      <div class="feature feature--fabric">• Luxury Fabric •</div>
    </div>

    <div class="dot-row" style="top:646px;">•••</div>
    <p class="eco-statement">This Tarnel skinny was proudly produced in an Oskel Platinum certified green plant with no negative environmental impact.</p>
    <div class="dot-row" style="top:738px;">•••</div>
  </section>
  <div class="caption" style="left:596px; top:878px;">BACK LABEL</div>

  <!-- Waist band label, option 1 -->
  <section class="label size-label size-wide">
    <div class="stitch"></div>
    <div class="size-row">
      <span class="num">32</span>
      <span class="dim">WAIST</span>
      <span class="times">x</span>
      <span class="num num--small">32</span>
      <span class="dim">LENGTH</span>
    </div>
  </section>
  <div class="caption" style="left:946px; top:228px;">WAIST BAND LABEL (opt 1)</div>

  <!-- Waist band label, option 2 -->
  <section class="label size-label size-tall">
    <div class="stitch"></div>
    <span class="num num--waist">32</span>
    <span class="dim dim--waist">WAIST</span>
    <span class="times">x</span>
    <span class="num num--length">32</span>
    <span class="dim">LENGTH</span>
  </section>
  <div class="caption" style="left:946px; top:552px;">WAIST BAND LABEL (opt 2)</div>

</body>
</html>
```